Room 4 Keeps Storage Poster Ad

Room 4 Keeps Storage needs an 8.5" X 11" specialty storage products poster.

Graphics that illustrate seasonal tire storage, bicycle storage, and motorcycle storage.

Information on the poster will be as follows:

Tire storage: $99.00/season + tax
bicycle storage: $99.00/season + tax
motorcycle storage: $250.00/season + tax
Phone: 306-517-4832
Web: www.room4keeps.ca
Address: Room 4 Keeps Storage, 4178 Draven Avenue, Saskatoon, SK, S7M 2R4

**Information does not need to be presented in this exact format. The designer can creatively list the services and the prices. The words phone, web, and address can be left out**

**The season that the ad is targeting is winter

Industry/Entity Type

Storage

```html
<!DOCTYPE html>
<html lang="en">
<head>
<meta charset="utf-8">
<title>Room 4 Keeps Storage – Seasonal Storage Poster</title>
<link rel="stylesheet" href="https://fonts.googleapis.com/css2?family=Josefin+Sans:wght@600;700&display=swap">
<style>
  :root {
    --brand-red: #d2262b;
    --soft-red: #e77a7d;
    --pale-red: #fbe3e3;
    --ink: #231f20;
    --frame: #333333;
    --paper: #ffffff;
  }
  * { margin: 0; padding: 0; box-sizing: border-box; }
  html, body {
    width: 933px; height: 1200px; overflow: hidden;
    background: var(--paper);
  }
  body { font-family: "Josefin Sans", Arial, sans-serif; color: var(--ink); }
  .poster { position: relative; width: 933px; height: 1200px; background: var(--paper); }
  .poster-frame {
    position: absolute; left: 54px; top: 48px; width: 833px; height: 1112px;
    border: 16px solid var(--frame);
  }
  .brand { position: absolute; left: 0; right: 0; top: 102px; text-align: center; }
  .brand-square {
    display: block; width: 84px; height: 84px; margin: 0 auto 26px;
    background: var(--brand-red);
  }
  .brand-name {
    font-weight: 700; font-size: 40px; line-height: 42px; letter-spacing: 1px;
    color: var(--ink); text-transform: uppercase;
  }
  .divider {
    position: absolute; left: 143px; width: 655px; height: 3px;
    background: repeating-linear-gradient(90deg, var(--brand-red) 0 18px, transparent 18px 31px);
  }
  .divider-top { top: 306px; }
  .divider-bottom { top: 1006px; }
  .categories {
    position: absolute; left: 90px; width: 746px; top: 320px;
    display: flex; justify-content: space-between;
    font-weight: 700; font-size: 24px; letter-spacing: 3px; text-transform: uppercase;
  }
  .service-panel {
    position: absolute; left: 142px; width: 373px; height: 199px;
    border: 3px solid var(--brand-red); padding: 14px 40px;
  }
  .service-art {
    width: 100%; height: 100%;
    background: radial-gradient(ellipse at center, var(--brand-red) 0%, var(--soft-red) 45%, var(--pale-red) 80%, var(--paper) 100%);
  }
  .panel-tires { top: 363px; }
  .panel-bicycles { top: 576px; }
  .panel-motorcycles { top: 790px; }
  .price { position: absolute; left: 596px; width: 160px; text-align: center; }
  .price-badge {
    width: 110px; height: 110px; margin: 0 auto;
    border: 3px solid var(--brand-red); border-radius: 50%;
    display: flex; align-items: center; justify-content: center;
    color: var(--brand-red); font-weight: 700; font-size: 32px; letter-spacing: 2px;
    padding-top: 6px;
  }
  .price-note {
    margin-top: 7px; color: var(--brand-red); font-weight: 700; font-size: 15px; letter-spacing: 1.5px;
  }
  .price-tires { top: 395px; }
  .price-bicycles { top: 602px; }
  .price-motorcycles { top: 824px; }
  .contact-row {
    position: absolute; left: 129px; width: 680px; top: 1050px;
    display: flex; justify-content: space-between;
    font-weight: 700; font-size: 24px; letter-spacing: 2.5px;
  }
  .contact-rule { position: absolute; left: 129px; width: 680px; top: 1084px; height: 3px; background: var(--ink); }
  .address {
    position: absolute; left: 0; right: 0; top: 1104px; text-align: center;
    font-weight: 700; font-size: 18px; letter-spacing: 1.5px;
  }
</style>
</head>
<body>
<main class="poster">
  <div class="poster-frame"></div>

  <header class="brand">
    <span class="brand-square"></span>
    <h1 class="brand-name">Room 4 Keeps<br>Storage</h1>
  </header>

  <div class="divider divider-top"></div>

  <nav class="categories">
    <span>Tires</span><span>Bicycles</span><span>Motorcycles</span><span>Whatever</span>
  </nav>

  <section class="service-panel panel-tires">
    <div class="service-art" role="img" aria-label="Red illustration of a stack of four tires"></div>
  </section>
  <div class="price price-tires">
    <div class="price-badge">$99</div>
    <p class="price-note">per season + HST</p>
  </div>

  <section class="service-panel panel-bicycles">
    <div class="service-art" role="img" aria-label="Red line illustration of a bicycle"></div>
  </section>
  <div class="price price-bicycles">
    <div class="price-badge">$99</div>
    <p class="price-note">per season + HST</p>
  </div>

  <section class="service-panel panel-motorcycles">
    <div class="service-art" role="img" aria-label="Red silhouette illustration of a sport motorcycle"></div>
  </section>
  <div class="price price-motorcycles">
    <div class="price-badge">$250</div>
    <p class="price-note">per season + HST</p>
  </div>

  <div class="divider divider-bottom"></div>

  <footer>
    <div class="contact-row">
      <span class="contact-phone">306-517-4832</span>
      <span class="contact-web">room4keeps.ca</span>
    </div>
    <div class="contact-rule"></div>
    <p class="address">4178 Draven Avenue, Saskatoon, SK, S7M 2R4</p>
  </footer>
</main>
</body>
</html>
```